The Corvanta Group's website for high impact furniture promotions

I am looking for a simple website. we are a promotional company that runs events for furniture stores to increase sales for short periods of time. i would like the website to have about 4 areas to explain our company. I would like it to be simple and user friendly. I would like a link to chatterbook and a contact section. I am attaching our logo that i would like somewhere large or possibly in the backround. I am open to different color schemes. I would like to convey fast paced, modern, reliable. I am open to all different styles and look forward to seeing whats out there. we are looking for a quick turn around, so if we see one that we like quick, we will pick that one thanks
Updates
Project Deadline Extended
Reason: looking for some really creative designs and want to give a fair amount of time to produce
Target Market(s)
Retail Furniture store owners
Industry/Entity Type
It Company
Number of Pages Required
1 page
Colors
Designer to choose colors to be used in the design.
Look and feel
Each slider illustrates characteristics of the customer's brand and the style your logo design should communicate.

```html
<!DOCTYPE html>
<html lang="en">
<head>
<meta charset="utf-8">
<title>The Corvanta Group</title>
<link href="https://fonts.googleapis.com/css2?family=Raleway:wght@400;500;600;700&family=Varela+Round&display=swap" rel="stylesheet">
<style>
:root{
  --brown-dark:#5f3716;
  --brown:#6b3e1a;
  --tan:#a67c52;
  --tan-text:#9b6a3c;
  --sand:#c4a287;
  --cream:#efe7df;
  --beige:#dcc9b8;
  --hero-bg:#f4f4f4;
  --card-bg:#f3f3f3;
  --ink:#3a2a1c;
  --muted:#6d6158;
  --star:#f2d21b;
  --white:#ffffff;
}
*{margin:0;padding:0;box-sizing:border-box}
html,body{width:1200px;height:1120px;overflow:hidden;background:var(--white)}
body{font-family:"Raleway",sans-serif;color:var(--ink)}
.stage{position:absolute;left:0;top:0;width:1500px;height:1400px;transform:scale(.8);transform-origin:0 0}
.page{position:absolute;left:457px;top:0;width:585px;height:1375px}
.abs{position:absolute}
.center{text-align:center}

/* top bar */
.topbar{left:0;top:0;width:585px;height:16px;background:var(--brown);color:var(--white);font-size:5px;white-space:nowrap}
.topbar .phone{left:80px;top:5px}
.topbar .social{left:215px;top:5px;width:150px;display:flex;justify-content:space-between}
.topbar .mail{right:80px;top:5px}
.topbar svg{vertical-align:-1px;margin-right:3px}

.hero{left:0;top:16px;width:585px;height:286px;background:var(--hero-bg)}

/* brand */
.brand{left:70px;top:22px;width:72px;text-align:center}
.brand-dot{width:26px;height:26px;border-radius:50%;background:var(--tan-text);margin:0 auto 3px}
.brand-name{font-size:7px;font-weight:600;color:var(--tan-text);letter-spacing:.5px;line-height:8px}
.brand-tag{font-size:3px;color:var(--tan-text);margin-top:2px}

/* nav */
.nav{left:150px;top:34px;width:362px;height:24px;background:var(--tan);display:flex;align-items:center;justify-content:flex-end;gap:18px;padding-right:18px;font-size:5px;color:var(--white)}
.nav .cart{display:flex;align-items:center;gap:2px}
.nav .badge{width:6px;height:6px;border-radius:50%;background:var(--white);color:var(--tan);font-size:4px;text-align:center;line-height:6px}

.hero-art{left:110px;top:95px;width:145px;height:145px;border-radius:50%;background:radial-gradient(circle at 55% 50%,#d98a6a 0 30%,var(--sand) 31%)}

.welcome{left:310px;top:108px;width:192px}
.welcome .kicker{font-family:"Varela Round",sans-serif;font-size:11px;letter-spacing:1px;color:var(--ink)}
.welcome h1{font-family:"Varela Round",sans-serif;font-size:17px;letter-spacing:1px;color:var(--tan-text);margin-top:7px}
.welcome p{font-size:5.6px;line-height:6.5px;color:var(--ink);margin-top:11px;padding:0 8px}
.btn{display:inline-block;border:1px solid var(--tan-text);border-radius:9px;font-size:4.6px;color:var(--ink);padding:4px 15px;background:transparent;white-space:nowrap}
.welcome .btn{margin-top:11px}

/* features */
.features{left:77px;top:280px;width:432px;height:43px;background:var(--brown);color:var(--white);display:flex;align-items:center;padding-left:17px}
.feature{display:flex;align-items:center;gap:8px;width:140px}
.feature .icon{width:26px;height:26px;border-radius:50%;background:var(--white);display:flex;align-items:center;justify-content:center}
.feature h3{font-size:7.5px;font-weight:500;letter-spacing:.3px}
.feature p{font-size:4px;margin-top:2px}

/* promos */
.promo{top:361px;width:216px;height:102px;padding:14px 17px}
.promo.left{left:77px;background:var(--cream)}
.promo.right{left:292px;background:var(--beige)}
.promo h3{font-size:7px;font-weight:500;letter-spacing:.4px;line-height:8px;color:var(--ink)}
.promo p{font-size:4px;line-height:5.5px;width:80px;margin-top:5px;color:var(--ink)}
.promo .btn{margin-top:7px;padding:3px 11px}
.promo-art{position:absolute;top:14px;right:16px;width:82px;height:74px;border-radius:2px}
.promo.left .promo-art{background:linear-gradient(160deg,#c98b4c,#7a3f17 60%,#2f1a0c)}
.promo.right .promo-art{left:122px;width:66px;background:linear-gradient(180deg,#5a3a1a,#2e1d10)}

/* section headings */
.section-head{left:0;width:585px;text-align:center}
.section-head .eyebrow{font-size:6px;color:var(--muted)}
.section-head h2{font-size:10px;font-weight:500;letter-spacing:1.4px;color:var(--brown);margin-top:5px}

/* products */
.arrow{font-size:13px;color:var(--muted);font-weight:400}
.product{top:544px;width:98px}
.product .art{height:113px;background:var(--card-bg);display:flex;align-items:center;justify-content:center}
.product .art span{display:block;width:62px;height:68px;border-radius:4px}
.product h4{font-size:6.2px;font-weight:500;color:var(--brown);margin-top:10px;text-align:center}
.stars{color:var(--star);font-size:7px;letter-spacing:-.5px;text-align:center;margin-top:3px;line-height:7px}
.price{text-align:center;font-size:6.5px;color:var(--ink);margin-top:3px}
.price s{font-size:3.5px;color:var(--muted);margin-left:2px;text-decoration:none}

/* subscribe & reviews */
.reviews-bg{left:0;top:761px;width:585px;height:177px;background:linear-gradient(90deg,#4a3019,#7a5533 30%,#6a4628 60%,#4d311a 85%,#8a6236)}
.reviews-bg::after{content:"";position:absolute;left:80px;right:100px;top:40px;height:120px;background:radial-gradient(ellipse at 50% 60%,rgba(150,110,70,.55),transparent 70%)}
.subscribe{left:77px;top:735px;width:432px;height:50px;background:var(--tan);color:var(--white);overflow:hidden}
.subscribe .ghost{left:160px;top:10px;font-family:"Varela Round",sans-serif;font-size:26px;letter-spacing:6px;color:rgba(255,255,255,.13)}
.subscribe .lead{left:20px;top:15px;font-size:7.4px;letter-spacing:.4px;line-height:8.5px;font-weight:500}
.subscribe .field{left:178px;top:18px;width:155px;border-bottom:1px solid rgba(255,255,255,.7);font-size:4.3px;padding-bottom:6px}
.subscribe .submit{left:360px;top:18px;border-color:var(--white);color:var(--white);padding:4px 15px}
.reviews-title{left:93px;top:836px;color:var(--white)}
.reviews-title .eyebrow{font-size:7px}
.reviews-title h2{font-size:13px;font-weight:700;letter-spacing:1.4px;margin-top:5px}
.reviews-title h3{font-size:11px;font-weight:400;letter-spacing:1.4px;margin-top:3px}
.avatar{left:283px;top:839px;width:38px;height:38px;border-radius:50%;background:var(--white);border:2px solid var(--white)}
.avatar span{display:block;width:100%;height:100%;border-radius:50%;background:linear-gradient(180deg,#c9a38c,#b94a3a)}
.quote{left:335px;top:841px;width:120px;color:var(--white);font-size:4.3px;line-height:5.2px}
.quote h4{font-size:6.6px;font-weight:500;margin-top:7px}
.reviews-arrow{color:var(--white);font-size:13px}

/* blog */
.post{top:1018px;width:134px}
.post .art{height:105px}
.post h4{font-size:6.6px;font-weight:500;color:var(--brown);text-align:center;margin-top:10px}
.post p{font-size:4.3px;line-height:5.5px;text-align:center;color:var(--ink);margin:4px 12px 0}

/* footer */
.footer{left:0;top:1209px;width:585px;height:166px;background:var(--brown-dark);color:var(--white)}
.footer h5{font-size:9px;font-weight:500;letter-spacing:.8px}
.col{top:31px}
.col p{font-size:4.5px;line-height:5.4px;margin-top:9px}
.col .more{font-weight:700;margin-top:6px;font-size:5px}
.col ul{list-style:none;margin-top:10px;font-size:4.8px}
.col li{margin-bottom:6px;display:flex;align-items:center;gap:4px}
.col li::before{content:"";width:2px;height:2px;border-radius:50%;background:var(--white)}
.contact-line{display:flex;align-items:flex-start;gap:5px;font-size:4.3px;line-height:5.3px;margin-top:6px}
.rule{left:0;top:136px;width:585px;height:1px;background:rgba(255,255,255,.35)}
.copy{left:0;top:148px;width:585px;text-align:center;font-size:4.6px}
</style>
</head>
<body>
<div class="stage">
<div class="page">

  <div class="abs topbar">
    <span class="abs phone"><svg width="5" height="5" viewBox="0 0 10 10"><path d="M2 1l2 2-1 1.5c.7 1.3 1.6 2.2 2.9 2.9L7.4 6l2 2-1.3 1.5C4.5 9.3.7 5.5.5 2.3z" fill="#fff"/></svg>0123 456 780</span>
    <span class="abs social"><span>chatterbook</span><span>chirper</span><span>pinboard</span><span>linkup</span><span>circleup</span></span>
    <span class="abs mail"><svg width="6" height="4" viewBox="0 0 12 8"><rect x=".5" y=".5" width="11" height="7" fill="none" stroke="#fff"/><path d="M.5.5L6 5l5.5-4.5" fill="none" stroke="#fff"/></svg>hello@corvanta.example</span>
  </div>

  <div class="abs hero"></div>

  <div class="abs brand">
    <div class="brand-dot"></div>
    <div class="brand-name">THE CORVANTA GROUP</div>
    <div class="brand-tag">High impact furniture promotions</div>
  </div>

  <nav class="abs nav">
    <span>Home</span><span>About Us</span><span>Services</span><span>Contact us</span>
    <svg width="6" height="6" viewBox="0 0 10 10"><circle cx="4" cy="4" r="3" fill="none" stroke="#fff" stroke-width="1.5"/><path d="M6.2 6.2L9 9" stroke="#fff" stroke-width="1.5"/></svg>
    <span class="cart"><svg width="8" height="6" viewBox="0 0 12 10"><path d="M0 1h2l2 6h6l1.5-4.5H3" fill="none" stroke="#fff"/><circle cx="5" cy="9" r="1" fill="#fff"/><circle cx="9" cy="9" r="1" fill="#fff"/></svg><span class="badge">0</span></span>
  </nav>

  <div class="abs hero-art" role="img" aria-label="Tufted coral upholstered antique side chair on a tan circle"></div>

  <div class="abs welcome center">
    <div class="kicker">Welcome To</div>
    <h1>Corvanta Group</h1>
    <p>Lorem Ipsum is simply dummy text of the printing and typesetting industry. Lorem Ipsum has been the industry's standard dummy text ever since the 1500s, when an unknown printer took a galley of type and scrambled it to make a type specimen book.</p>
    <span class="btn">Read More</span>
  </div>

  <div class="abs features">
    <div class="feature">
      <div class="icon"><svg width="13" height="11" viewBox="0 0 14 12"><rect x="2" y="1" width="10" height="5" rx="1" fill="#6b3e1a"/><rect x="0" y="5" width="14" height="4" rx="1" fill="#6b3e1a"/><rect x="1" y="9" width="1.5" height="2" fill="#6b3e1a"/><rect x="11.5" y="9" width="1.5" height="2" fill="#6b3e1a"/></svg></div>
      <div><h3>Your Heading</h3><p>Lorem Ipsum is simply dummy text</p></div>
    </div>
    <div class="feature">
      <div class="icon"><svg width="12" height="12" viewBox="0 0 12 12"><path d="M6 0v3M2 5h8M6 3l-4 2 1 3h6l1-3z" fill="none" stroke="#6b3e1a"/><rect x="1" y="9" width="10" height="2" fill="#6b3e1a"/></svg></div>
      <div><h3>Your Heading</h3><p>Lorem Ipsum is simply dummy text</p></div>
    </div>
    <div class="feature">
      <div class="icon"><svg width="11" height="12" viewBox="0 0 11 12"><ellipse cx="5.5" cy="4" rx="5" ry="3.5" fill="#6b3e1a"/><rect x="4.5" y="7" width="2" height="3" fill="#6b3e1a"/><rect x="2" y="10" width="7" height="1.5" fill="#6b3e1a"/></svg></div>
      <div><h3>Your Heading</h3><p>Lorem Ipsum is simply dummy text</p></div>
    </div>
  </div>

  <div class="abs promo left">
    <h3>Your Heading<br>Goes Here</h3>
    <p>Lorem Ipsum is simply dummy text of the printing and typesetting industry. Lorem Ipsum has been the industry's</p>
    <span class="btn">Shop Now</span>
    <div class="promo-art" role="img" aria-label="Wooden dining table with high-back chairs"></div>
  </div>
  <div class="abs promo right">
    <h3>Your Heading<br>Goes Here</h3>
    <p>Lorem Ipsum is simply dummy text of the printing and typesetting industry. Lorem Ipsum has been the industry's</p>
    <span class="btn">Shop Now</span>
    <div class="promo-art" role="img" aria-label="Dark wooden glass-front display cabinet"></div>
  </div>

  <div class="abs section-head" style="top:492px">
    <div class="eyebrow">Corvanta Group</div>
    <h2>FEATURED PRODUCTS</h2>
  </div>

  <span class="abs arrow" style="left:47px;top:593px">&#8249;</span>
  <span class="abs arrow" style="left:530px;top:593px">&#8250;</span>

  <div class="abs product" style="left:76px">
    <div class="art"><span role="img" aria-label="Blue plastic chair on castors" style="background:linear-gradient(180deg,#3a5a80 0 55%,#c9c9c9 56%)"></span></div>
    <h4>Your Heading Goes Here</h4><div class="stars">&#9733;&#9733;&#9733;&#9733;&#9733;</div>
    <div class="price">$19.00<s>$26.00</s></div>
  </div>
  <div class="abs product" style="left:188px">
    <div class="art"><span role="img" aria-label="Carved wooden side table" style="background:linear-gradient(180deg,#8a5528,#5e3414)"></span></div>
    <h4>Your Heading Goes Here</h4><div class="stars">&#9733;&#9733;&#9733;&#9733;&#9733;</div>
    <div class="price">$19.00<s>$26.00</s></div>
  </div>
  <div class="abs product" style="left:299px">
    <div class="art"><span role="img" aria-label="Black grand piano" style="background:linear-gradient(180deg,#2a2a2a,#0d0d0d)"></span></div>
    <h4>Your Heading Goes Here</h4><div class="stars">&#9733;&#9733;&#9733;&#9733;&#9733;</div>
    <div class="price">$19.00<s>$26.00</s></div>
  </div>
  <div class="abs product" style="left:410px">
    <div class="art"><span role="img" aria-label="Dining set with cream table and dark chairs" style="background:linear-gradient(180deg,#3a2418,#d9c9aa 55%,#3a2418)"></span></div>
    <h4>Your Heading Goes Here</h4><div class="stars">&#9733;&#9733;&#9733;&#9733;&#9733;</div>
    <div class="price">$19.00<s>$26.00</s></div>
  </div>

  <div class="abs reviews-bg" role="img" aria-label="Patterned sofa with cushions and a lit table lamp in a warm living room"></div>

  <div class="abs subscribe">
    <span class="abs ghost">SUBSCRIBE</span>
    <div class="abs lead">Subscribe To Say Update With<br>Latest News And Discounts</div>
    <div class="abs field">Enter Your Email Address</div>
    <span class="abs btn submit">Submit</span>
  </div>

  <div class="abs reviews-title">
    <div class="eyebrow">Corvanta Group</div>
    <h2>CUSTOMERS</h2>
    <h3>REVIEWS</h3>
  </div>
  <span class="abs reviews-arrow" style="left:240px;top:851px">&#8249;</span>
  <span class="abs reviews-arrow" style="left:484px;top:851px">&#8250;</span>
  <div class="abs avatar"><span role="img" aria-label="Customer portrait"></span></div>
  <div class="abs quote">
    Lorem Ipsum is simply dummy text of the printing and typesetting industry. Lorem Ipsum has been the industry's standard dummy text ever since the 1500s.
    <h4>Your Heading</h4>
  </div>

  <div class="abs section-head" style="top:969px">
    <div class="eyebrow">Corvanta Group</div>
    <h2>RECENT BLOG</h2>
  </div>

  <span class="abs arrow" style="left:47px;top:1064px">&#8249;</span>
  <span class="abs arrow" style="left:530px;top:1064px">&#8250;</span>

  <div class="abs post" style="left:77px">
    <div class="art" role="img" aria-label="Bright living room with light sofa" style="background:linear-gradient(180deg,#e8e4de,#cfc6bb 60%,#8d8378)"></div>
    <h4>Your Heading Goes Here</h4>
    <p>Lorem Ipsum is simply dummy text of the printing and typesetting industry. Lorem Ipsum has been the industry's standard dummy text ever since the 1500s.</p>
  </div>
  <div class="abs post" style="left:225px">
    <div class="art" role="img" aria-label="Living room with wooden units and dark armchair" style="background:linear-gradient(180deg,#e9e2d6,#c89048 55%,#6b4a2c)"></div>
    <h4>Your Heading Goes Here</h4>
    <p>Lorem Ipsum is simply dummy text of the printing and typesetting industry. Lorem Ipsum has been the industry's standard dummy text ever since the 1500s.</p>
  </div>
  <div class="abs post" style="left:374px">
    <div class="art" role="img" aria-label="Round dark dining table with upholstered chairs" style="background:linear-gradient(180deg,#d9d2c9,#4a2a22 55%,#b9aea3)"></div>
    <h4>Your Heading Goes Here</h4>
    <p>Lorem Ipsum is simply dummy text of the printing and typesetting industry. Lorem Ipsum has been the industry's standard dummy text ever since the 1500s.</p>
  </div>

  <footer class="abs footer">
    <div class="abs col" style="left:77px;width:100px">
      <h5>About Us</h5>
      <p>Lorem Ipsum is simply dummy text of the printing and typesetting industry. Lorem Ipsum has been the industry's standard dummy text ever since the 1500s, when an unknown printer took a galley of type and scrambled it to make a type specimen book.</p>
      <p class="more">Read More</p>
    </div>
    <div class="abs col" style="left:264px;width:100px">
      <h5>Quick Links</h5>
      <ul><li>Home</li><li>About Us</li><li>Services</li><li>Contact Us</li></ul>
    </div>
    <div class="abs col" style="left:412px;width:100px">
      <h5>Contact Us</h5>
      <p>Lorem Ipsum is simply dummy text of the printing and typesetting industry.</p>
      <div class="contact-line"><svg width="5" height="6" viewBox="0 0 10 12"><path d="M5 0a4 4 0 0 0-4 4c0 3 4 8 4 8s4-5 4-8a4 4 0 0 0-4-4z" fill="#fff"/><circle cx="5" cy="4" r="1.5" fill="#5f3716"/></svg><span>Lorem Ipsum is simply<br>dummy text of the printing</span></div>
      <div class="contact-line"><svg width="5" height="5" viewBox="0 0 10 10"><path d="M2 1l2 2-1 1.5c.7 1.3 1.6 2.2 2.9 2.9L7.4 6l2 2-1.3 1.5C4.5 9.3.7 5.5.5 2.3z" fill="#fff"/></svg><span>012 555 0148</span></div>
      <div class="contact-line"><svg width="6" height="4" viewBox="0 0 12 8"><rect x=".5" y=".5" width="11" height="7" fill="none" stroke="#fff"/><path d="M.5.5L6 5l5.5-4.5" fill="none" stroke="#fff"/></svg><span>info@corvanta.example</span></div>
    </div>
    <div class="abs rule"></div>
    <div class="abs copy">Copyright &copy; 2017 Corvanta Group - All Rights Reserved</div>
  </footer>

</div>
</div>
</body>
</html>
```